Rural contractor needs professional informative business card

We need a business card design that looks professional but also includes information about the services that the business offers.
The business is an earthmoving and transport business. All of the services offered are listed on the old card attached.
The business is aimed at farmers so the design we are after is a classic look. The card needs to include all of the information that is listed on the old card design uploaded as an attachment. We recognize that this is a lot of information to fit on a business card but it also operates as a key marketing tool so is very important to the business.
Feel free to send me your questions.
Thanks
Reason: We are having trouble deciding between all these great designs - thank you for your efforts
We would love to see some designs using red with a little white and black. Also feel free to re-design our logo if you feel it needs to be to fit your designs. Thank you

```html
<!DOCTYPE html>
<html lang="en">
<head>
<meta charset="utf-8">
<title>RT Callister Contracting – Business Card</title>
<link href="https://fonts.googleapis.com/css2?family=Roboto+Condensed:wght@400;700&display=swap" rel="stylesheet">
<style>
  :root {
    --stage: #1c1713;
    --soil: #3a322c;
    --soil-dark: #231d19;
    --yellow: #f6e21a;
    --yellow-deep: #e8c80c;
    --ink: #141210;
    --white: #ffffff;
    --stone: #c9c3b8;
  }
  * { box-sizing: border-box; margin: 0; padding: 0; }
  html, body {
    width: 1200px; height: 675px; overflow: hidden;
    background: var(--stage);
    font-family: "Roboto Condensed", Arial, sans-serif;
  }
  .cards {
    position: relative; width: 1200px; height: 675px;
    display: flex; gap: 40px; justify-content: center; align-items: center;
  }
  .card {
    position: relative; width: 560px; height: 330px; overflow: hidden;
    box-shadow: 0 8px 24px rgba(0,0,0,.6);
  }

  /* Front */
  .card-front { background: var(--soil); }
  .front-tab { position: absolute; background: var(--yellow); width: 12px; height: 44px; }
  .front-tab.left { left: 12px; top: 168px; }
  .front-tab.right { right: 12px; top: 70px; }
  .front-brand {
    position: absolute; left: 90px; top: 62px; color: var(--stone); text-align: center;
  }
  .front-brand .name { font-size: 66px; font-weight: 700; letter-spacing: -1px; line-height: 1; }
  .front-brand .sub { font-size: 22px; font-weight: 700; letter-spacing: 12px; margin-top: 10px; }
  .contact { position: absolute; color: var(--white); font-size: 14px; display: flex; align-items: center; gap: 6px; }
  .contact svg { width: 14px; height: 14px; fill: var(--yellow); }
  .contact.phone { right: 34px; top: 208px; font-size: 15px; }
  .contact.address { right: 34px; top: 230px; }
  .contact.email { left: 40px; top: 262px; font-size: 13px; }
  .tagline {
    position: absolute; left: 0; right: 0; bottom: 0; height: 48px;
    background: var(--yellow); color: var(--ink);
    font-size: 25px; font-weight: 700; text-align: center; line-height: 48px;
  }

  /* Back */
  .card-back { background: var(--yellow); }
  .back-left { position: absolute; left: 0; top: 0; width: 178px; height: 100%; background: var(--soil); }
  .back-stripe { position: absolute; left: 178px; top: 0; width: 22px; height: 100%; background: var(--yellow); }
  .back-rule { position: absolute; left: 200px; top: 0; width: 6px; height: 100%; background: var(--ink); }
  .back-field {
    position: absolute; left: 206px; top: 0; right: 0; height: 100%;
    background: radial-gradient(ellipse at 60% 40%, #f3d64a 0%, var(--yellow) 55%, var(--yellow-deep) 100%);
  }
  .back-brand {
    position: absolute; left: 22px; top: 40px; color: var(--ink); background: var(--yellow);
    padding: 4px 10px 5px; text-align: center;
  }
  .back-brand .name { font-size: 26px; font-weight: 700; line-height: 1; letter-spacing: -.5px; }
  .back-brand .sub { font-size: 10px; font-weight: 700; letter-spacing: 5px; margin-top: 3px; }
  .truck-photo {
    position: absolute; left: 20px; top: 168px; width: 250px; height: 162px;
    background: linear-gradient(160deg, #e9ecef 0%, #a7afb6 45%, #4b4a48 80%, #2a2624 100%);
  }
  .services { position: absolute; right: 18px; text-align: right; color: var(--ink); }
  .services.earth { top: 78px; }
  .services.transport { top: 200px; }
  .services h2 {
    display: inline-block; background: var(--soil-dark); color: var(--white);
    font-size: 15px; font-weight: 700; letter-spacing: 1px;
    padding: 3px 12px 3px 34px; margin-bottom: 6px;
  }
  .services ul { list-style: none; font-size: 15px; line-height: 17px; }
  .services li::after { content: " \25C6"; font-size: 9px; vertical-align: 2px; }
</style>
</head>
<body>
<main class="cards">
  <section class="card card-front" aria-label="Card front">
    <div class="front-tab left"></div>
    <div class="front-tab right"></div>
    <div class="front-brand">
      <div class="name">RT Callister</div>
      <div class="sub">CONTRACTING</div>
    </div>
    <div class="contact phone">0400 217 384
      <svg viewBox="0 0 24 24"><path d="M6.6 10.8a15.1 15.1 0 0 0 6.6 6.6l2.2-2.2a1 1 0 0 1 1-.25 11.4 11.4 0 0 0 3.6.57 1 1 0 0 1 1 1V20a1 1 0 0 1-1 1A17 17 0 0 1 3 4a1 1 0 0 1 1-1h3.5a1 1 0 0 1 1 1c0 1.25.2 2.45.57 3.57a1 1 0 0 1-.25 1z"/></svg>
    </div>
    <div class="contact address">42 Wattle Street, Dunmore 2830
      <svg viewBox="0 0 24 24"><path d="M12 3 2 12h3v8h5v-5h4v5h5v-8h3z"/></svg>
    </div>
    <div class="contact email">
      <svg viewBox="0 0 24 24"><path d="M2 5h20v14H2z M2 5l10 8 10-8" stroke="#3a322c" stroke-width="1.5"/></svg>
      rtcallister@mailbox.com
    </div>
    <div class="tagline">Earthmoving &amp; Transport Solutions</div>
  </section>

  <section class="card card-back" aria-label="Card back">
    <div class="back-left"></div>
    <div class="back-stripe"></div>
    <div class="back-rule"></div>
    <div class="back-field" role="img" aria-label="Faded photograph of earthmoving machinery in a paddock, yellow tinted"></div>
    <div class="back-brand">
      <div class="name">RT Callister</div>
      <div class="sub">CONTRACTING</div>
    </div>
    <div class="truck-photo" role="img" aria-label="Photograph of a white prime mover truck on a dirt road"></div>
    <div class="services earth">
      <h2>EARTHMOVING</h2>
      <ul>
        <li>Road Building &amp; Maintenance</li>
        <li>Poly Pipe Laying</li>
        <li>Clearing fence lines</li>
        <li>Sand &amp; Gravel supplies</li>
      </ul>
    </div>
    <div class="services transport">
      <h2>TRANSPORT</h2>
      <ul>
        <li>Grain</li>
        <li>Cotton</li>
        <li>Sand &amp; Gravel</li>
        <li>Wool</li>
      </ul>
    </div>
  </section>
</main>
</body>
</html>
```